Business Card for a new businees.

need a very good business for a new company based in Riverside California call Levy Lantern LLC. We help client file taxes, resolve tax debt and attain peace of mind We help people nationwide solve Tax problems. We help with Installment agreements, Offers in Compromise, Partial Pay Installment Agreements, Currently Not Collectible status, Liens and Levy Removal, Garnishment removal. We offer individualized services

Target Market(s)

Any one with Tax Problems nationwide. My clients span across age, occupation etc

Contact Information for Business Card

Card must be attractive and have enough information to let client know we care and call us

Colors

Designer to choose colors to be used in the design.

Requirements
Must have
• the basics and then surprise me
Nice to have
• surprise m

```html
<!DOCTYPE html>
<html lang="en">
<head>
<meta charset="utf-8">
<title>Levy Lantern LLC – Business Card</title>
<link rel="stylesheet" href="https://fonts.googleapis.com/css2?family=Arimo:wght@400;700&display=swap">
<style>
  :root {
    --stage: #999999;
    --paper: #ffffff;
    --olive: #9a8122;
    --olive-dark: #8c7420;
    --gold: #c9a11a;
    --yellow: #f5d040;
    --ink: #222222;
    --ink-soft: #333333;
  }
  * { margin: 0; padding: 0; box-sizing: border-box; }
  html, body { width: 1200px; height: 900px; overflow: hidden; }
  body {
    position: relative;
    background: var(--stage);
    font-family: "Arimo", Arial, sans-serif;
  }
  .card {
    position: absolute;
    top: 306px;
    height: 272px;
    box-shadow: 2px 3px 4px rgba(0,0,0,0.45);
    overflow: hidden;
  }
  .card--front { left: 150px; width: 438px; background: var(--paper); }
  .card--back  { left: 608px; width: 441px; background: var(--olive); color: #fff; }

  .front__accent { position: absolute; left: 0; top: 26px; }
  .holder { position: absolute; left: 36px; top: 30px; }
  .holder__name { font-size: 15px; font-weight: 700; color: var(--gold); letter-spacing: 0.2px; }
  .holder__title { font-size: 12.5px; color: var(--ink-soft); margin-top: 1px; }

  .brand {
    position: absolute; left: 195px; top: 100px;
    display: flex; align-items: center; gap: 10px;
  }
  .brand__dot { width: 14px; height: 14px; border-radius: 50%; background: var(--gold); }
  .brand__name { font-size: 28px; font-weight: 700; color: var(--gold); letter-spacing: -0.5px; }

  .contact { position: absolute; left: 23px; top: 209px; font-size: 12.5px; color: var(--ink-soft); }
  .contact__row { display: flex; align-items: center; gap: 4px; height: 16px; }
  .contact__row svg { width: 9px; height: 9px; }

  .phone {
    position: absolute; right: 22px; top: 220px;
    display: flex; align-items: center; gap: 3px;
    font-size: 18px; color: var(--ink);
  }
  .front__bands { position: absolute; left: 0; bottom: 0; }

  .back__brand {
    position: absolute; left: 18px; top: 118px; width: 175px;
    display: flex; align-items: center; justify-content: center; gap: 8px;
  }
  .back__brand-dot { width: 14px; height: 14px; border-radius: 50%; background: #fff; }
  .back__brand-name { font-size: 24px; font-weight: 700; color: #fff; }

  .services { position: absolute; left: 209px; top: 78px; list-style: none; font-size: 13px; }
  .services li { height: 19.8px; display: flex; align-items: center; }
  .services li::before {
    content: ""; width: 6px; height: 6px; border-radius: 50%;
    background: #fff; margin-right: 5px;
  }
  .promise {
    position: absolute; left: 95px; top: 227px;
    font-size: 13px; font-weight: 700; letter-spacing: 0.2px;
  }
</style>
</head>
<body>
  <section class="card card--front" aria-label="Business card front">
    <svg class="front__accent" width="28" height="37" viewBox="0 0 28 37" aria-hidden="true">
      <polygon points="0,0 10,0 15,37 0,37" fill="var(--olive-dark)"/>
      <polygon points="12,0 27,0 27,37 17,37" fill="var(--yellow)"/>
    </svg>
    <div class="holder">
      <p class="holder__name">DANIEL HARPER</p>
      <p class="holder__title">Managing Director</p>
    </div>

    <div class="brand">
      <span class="brand__dot"></span>
      <span class="brand__name">Levy Lantern</span>
    </div>

    <div class="contact">
      <p class="contact__row">
        <svg viewBox="0 0 10 10" aria-hidden="true"><rect x="0" y="1.5" width="10" height="7" fill="var(--gold)"/><polyline points="0,1.5 5,5.5 10,1.5" fill="none" stroke="#fff" stroke-width="1"/></svg>
        info@levylantern.com
      </p>
      <p class="contact__row">
        <svg viewBox="0 0 10 10" aria-hidden="true"><circle cx="5" cy="5" r="5" fill="var(--gold)"/><path d="M3 3 L6 4 L5 7 Z" fill="#fff"/></svg>
        www.levylantern.com
      </p>
    </div>

    <p class="phone">444 555 0142
      <svg width="12" height="16" viewBox="0 0 12 16" aria-hidden="true"><path d="M3 1 L6 4 L4.5 6 C5 8.5 6.5 10.5 8 11.5 L10 10 L12 13 L10 15.5 C5 15 1 9 1 3.5 Z" fill="var(--yellow)"/></svg>
    </p>

    <svg class="front__bands" width="438" height="20" viewBox="0 0 438 20" aria-hidden="true">
      <rect x="0" y="5" width="215" height="15" fill="var(--olive-dark)"/>
      <polygon points="220,0 438,0 438,20 205,20" fill="var(--yellow)"/>
    </svg>
  </section>

  <section class="card card--back" aria-label="Business card back">
    <div class="back__brand">
      <span class="back__brand-dot"></span>
      <span class="back__brand-name">Levy Lantern</span>
    </div>
    <ul class="services">
      <li>Installment agreements</li>
      <li>Offers in Compromise</li>
      <li>Partial Pay Installment Agreements</li>
      <li>Currently Not Collectible status</li>
      <li>Liens and Levy Removal</li>
      <li>Garnishment removal.</li>
    </ul>
    <p class="promise">WE OFFER INDIVIDUALIZED SERVICES.</p>
  </section>
</body>
</html>
```